Redesign of a Brochure based on an exsiting example for Web download and email marketing

Can you create a professional brochure based on the attached PDF. We need to keep the name, the logo and the content but everything else can be changed . The PDF will primarily be will be used for web download and email marking but it aslo be printed out for a poster design will be appropriate

Target Market(s)

Business to Business

Industry/Entity Type

Marketing

Font styles to use
Serif

Requirements
Must have
• Must have the existing logo ( in the attached document) and contain the same content

```html
<!DOCTYPE html>
<html lang="en">
<head>
<meta charset="utf-8">
<title>IT Run Model 1 – Veridane</title>
<link rel="stylesheet" href="https://fonts.googleapis.com/css2?family=Tinos:wght@400;700&family=Arimo:wght@400&family=Roboto+Condensed:wght@700&family=Michroma&family=Open+Sans:wght@400&display=swap">
<style>
  :root {
    --navy: #0d4479;
    --ink: #1f2226;
    --charcoal: #25282c;
    --paper: #ffffff;
    --text: #1d1d1d;
  }
  * { margin: 0; padding: 0; box-sizing: border-box; }
  html, body { width: 1200px; height: 907px; overflow: hidden; background: var(--paper); }
  .brochure { position: relative; width: 1200px; height: 907px; background: var(--paper); overflow: hidden; }
  .artwork { position: absolute; inset: 0; }

  .brand-name {
    position: absolute; left: 36px; top: 112px;
    font-family: "Tinos", serif; font-weight: 400; font-size: 30px;
    letter-spacing: 7px; color: var(--paper);
  }

  .model-title {
    position: absolute; left: 36px; top: 268px;
    font-family: "Tinos", serif; font-weight: 700; font-size: 38px; line-height: 42px;
    color: var(--navy); letter-spacing: 0.5px;
  }
  .model-copy {
    position: absolute; left: 36px; top: 318px; width: 482px;
    font-family: "Arimo", sans-serif; font-size: 15px; line-height: 18.4px;
    color: var(--text); text-align: justify;
  }
  .model-copy p + p { margin-top: 4px; }

  .facts {
    position: absolute; left: 640px; width: 545px; top: 306px;
    text-align: center;
  }
  .fact-label {
    font-family: "Roboto Condensed", sans-serif; font-weight: 700;
    font-size: 38px; color: var(--navy); line-height: 44px;
  }
  .fact-value {
    font-family: "Michroma", sans-serif; font-size: 35px; color: var(--ink);
    line-height: 50px; letter-spacing: 2px;
  }
  .fact-value.model-number { letter-spacing: 6px; font-size: 32px; }
  .fact-date { margin-bottom: 18px; }

  .author-bar {
    position: absolute; left: 657px; top: 521px; width: 492px; height: 58px;
    background: var(--charcoal); color: var(--paper);
    font-family: "Roboto Condensed", sans-serif; font-weight: 700; font-size: 34px;
    display: flex; align-items: center; justify-content: center; letter-spacing: 0.5px;
  }
  .contact {
    position: absolute; left: 640px; width: 545px; top: 606px; text-align: center;
  }
  .contact-label {
    font-family: "Roboto Condensed", sans-serif; font-weight: 700; font-size: 25px; color: var(--navy);
  }
  .contact-email {
    font-family: "Arimo", sans-serif; font-size: 22px; letter-spacing: 3.2px; color: var(--ink); margin-top: 4px;
  }

  .related {
    position: absolute; right: 63px; top: 793px; text-align: right;
    font-family: "Open Sans", sans-serif; font-size: 22px; line-height: 33px; color: var(--paper);
  }

  .chart-label { font-family: "Arimo", sans-serif; font-size: 8px; fill: #333; }
  .chart-title { font-family: "Arimo", sans-serif; font-size: 9.5px; fill: #111; }
</style>
</head>
<body>
<main class="brochure">
  <svg class="artwork" width="1200" height="907" viewBox="0 0 1200 907" xmlns="http://www.w3.org/2000/svg">
    <defs>
      <linearGradient id="skyline" x1="0" y1="0" x2="0" y2="1">
        <stop offset="0" stop-color="#ffffff" stop-opacity="0"/>
        <stop offset="0.45" stop-color="#cbd7e6" stop-opacity="0.55"/>
        <stop offset="1" stop-color="#8fa4bd" stop-opacity="0.7"/>
      </linearGradient>
      <linearGradient id="team-photo" x1="0" y1="0" x2="1" y2="1">
        <stop offset="0" stop-color="#e9ecef"/>
        <stop offset="0.5" stop-color="#b9b2aa"/>
        <stop offset="1" stop-color="#6e6a66"/>
      </linearGradient>
      <linearGradient id="globe-photo" x1="0" y1="0" x2="1" y2="1">
        <stop offset="0" stop-color="#4a5666"/>
        <stop offset="0.5" stop-color="#9aa7b5"/>
        <stop offset="1" stop-color="#2c3440"/>
      </linearGradient>
      <linearGradient id="growth-photo" x1="0" y1="0" x2="1" y2="1">
        <stop offset="0" stop-color="#1d2430"/>
        <stop offset="0.55" stop-color="#6f8fb0"/>
        <stop offset="1" stop-color="#b9d6ee"/>
      </linearGradient>
    </defs>

    <!-- city skyline backdrop -->
    <rect class="skyline-backdrop" x="610" y="540" width="590" height="260" fill="url(#skyline)" role="img" aria-label="Faded photograph of a city skyline across a river at dusk"/>
    <rect class="skyline-backdrop" x="0" y="620" width="610" height="200" fill="url(#skyline)" opacity="0.6"/>

    <!-- top band -->
    <polygon class="top-band" points="0,0 1200,0 1200,40 0,222" fill="var(--navy)"/>
    <polygon class="top-rule" points="0,246 1200,60 1200,74 0,260" fill="var(--ink)"/>

    <!-- page fold -->
    <line class="fold" x1="609" y1="0" x2="609" y2="907" stroke="#000" stroke-opacity="0.06" stroke-width="2"/>

    <!-- bottom band -->
    <polygon class="bottom-rule" points="0,875 1200,705 1200,715 0,885" fill="var(--navy)"/>
    <polygon class="bottom-band" points="0,893 1200,723 1200,907 0,907" fill="var(--charcoal)"/>

    <!-- photo hexagons -->
    <g class="hex-photo">
      <polygon points="491,12 618,70 618,205 491,268 365,205 365,70" fill="var(--paper)" stroke="var(--navy)" stroke-width="6"/>
      <polygon points="491,24 608,78 608,198 491,256 375,198 375,78" fill="url(#team-photo)" role="img" aria-label="Photograph of a business team working together at a laptop"/>
    </g>
    <g class="hex-photo">
      <polygon points="771,12 885,70 885,205 771,268 657,205 657,70" fill="var(--paper)" stroke="var(--navy)" stroke-width="6"/>
      <polygon points="771,24 875,78 875,198 771,256 667,198 667,78" fill="url(#globe-photo)" role="img" aria-label="Photograph of a hand touching a glowing world map network"/>
    </g>
    <g class="hex-photo">
      <polygon points="118,668 214,718 214,822 118,872 22,822 22,718" fill="var(--paper)" stroke="var(--navy)" stroke-width="6"/>
      <polygon points="118,680 204,725 204,815 118,860 32,815 32,725" fill="url(#growth-photo)" role="img" aria-label="Photograph of a businessman drawing a rising growth graph"/>
    </g>

    <!-- pie chart -->
    <g class="tower-chart">
      <text class="chart-title" x="380" y="674" text-anchor="middle">Tech Towers (Run Build Manage)</text>
      <path d="M380,745 L346.6,705.2 A52,52 0 0 1 432,745 Z" fill="#f9b752"/>
      <path d="M380,745 L432,745 A52,52 0 0 1 422.6,774.8 Z" fill="#c48cf0"/>
      <path d="M380,745 L422.6,774.8 A52,52 0 0 1 419.8,778.4 Z" fill="#8fd15a"/>
      <path d="M380,745 L419.8,778.4 A52,52 0 0 1 337.4,774.8 Z" fill="#5cb8ef"/>
      <path d="M380,745 L337.4,774.8 A52,52 0 0 1 328.8,736 Z" fill="#ef6a6a"/>
      <path d="M380,745 L328.8,736 A52,52 0 0 1 346.6,705.2 Z" fill="#f6f173"/>
      <text class="chart-label" x="400" y="688">Apps Maintenance</text>
      <text class="chart-label" x="344" y="714" text-anchor="end">Datacentre &amp; Servers</text>
      <text class="chart-label" x="436" y="764">Helpdesk &amp; Ops Bridge</text>
      <text class="chart-label" x="324" y="758" text-anchor="end">End User Computing</text>
      <text class="chart-label" x="428" y="784">Not Allocated</text>
      <text class="chart-label" x="380" y="812" text-anchor="middle">Networks &amp; Telecoms</text>
    </g>
  </svg>

  <div class="brand-name">VERIDANE</div>

  <h1 class="model-title">IT RUN MODEL 1</h1>
  <section class="model-copy">
    <p>IT Run Model 1 is a simple IT costing modelsuitable for any industry. It is designed to support a sophisticated level of cost transparency across common IT technologies, towers and services with a minimum of effort. As a starting point this model is mainly focused on the IT costs that“run” the business. However, it can be extended to cover a detailed view of IT investments that “change” the business as well. In addition, it can be used as a starting point to manage demand by extending support for specific<br>business processes.</p>
    <p>This model is a concrete implementation of the Technology Business Management (TBM) standard framework.*TBM has three main views : a Finance View, an IT View and a Business view. This model implements these views through three simple layers ; IT Cost centres, IT Technology Towers and Products &amp; Services. You can start by implementing just the IT Cost Centres to get some valuable insights before moving on to the IT Towers and<br>Product/Services layers</p>
  </section>

  <section class="facts">
    <div class="fact-label">DATE PUBLISHED</div>
    <div class="fact-value fact-date">05 JUNE 2015</div>
    <div class="fact-label">PUBLISHED MODEL NUMBER:</div>
    <div class="fact-value model-number">100001</div>
  </section>

  <div class="author-bar">AUTHOR: VERIDANE</div>

  <section class="contact">
    <div class="contact-label">CONTACT US</div>
    <div class="contact-email">enquiries@ashcombehill.co.uk</div>
  </section>

  <section class="related">
    <div>Related models:</div>
    <div>IT Build Model 1 - 100002</div>
  </section>
</main>
</body>
</html>
```